URGENT Conference Banner ad to attract a crowd!

I need please in my brand colours 2 x static ads with this copy please:
Have an online business?
Make your customers stick!
It really needs to stand out but not be offensive.
I would like to see blue background on white font and then the reverse. on the white one, it needs a thin blue border around it.
I need it in static: 300x250 and 300x600.
on this one - 300x600. please add a circle saying register now!
Please see examples of other messages I have done. I need this URGENTLY pelase :)
Target Market(s)
http://www.tradefairvantora.com.au/en/home/
Industry/Entity Type
Business
Font styles to use
Other font styles liked:
- roboto font
Requirements
Must have
- Use this blue:
- 00b6ce
- roboto font
Nice to have
- look and feel like my banners supplied

```html
<!DOCTYPE html>
<html lang="en">
<head>
<meta charset="utf-8">
<title>Have an online business? – Banner 300x600</title>
<link rel="stylesheet" href="https://fonts.googleapis.com/css2?family=Roboto:wght@300;700&display=swap">
<style>
  :root {
    --brand-blue: #00bfd6;
    --tint-blue: #dcf5f8;
    --white: #ffffff;
    --page-bg: #ffffff;
  }
  html, body {
    margin: 0;
    padding: 0;
    width: 1200px;
    height: 1000px;
    overflow: hidden;
    background: var(--page-bg);
  }
  .stage {
    position: relative;
    width: 1200px;
    height: 1000px;
  }
  .banner {
    position: absolute;
    left: 431px;
    top: 199px;
    width: 300px;
    height: 600px;
    box-sizing: border-box;
    border: 3px solid var(--brand-blue);
    background: var(--white);
    overflow: hidden;
    font-family: "Roboto", Arial, sans-serif;
    color: var(--brand-blue);
  }
  .shop-illustration {
    position: absolute;
    left: 66px;
    top: 112px;
    width: 226px;
    height: 320px;
    border-radius: 10px;
    background: linear-gradient(160deg, #e4f8fa 0%, var(--tint-blue) 100%);
    transform: rotate(8deg);
    transform-origin: center;
  }
  .headline {
    position: absolute;
    left: 13px;
    top: 19px;
    margin: 0;
    font-weight: 700;
    font-size: 44px;
    line-height: 54px;
    letter-spacing: 1px;
    text-transform: uppercase;
  }
  .subline {
    position: absolute;
    left: 13px;
    top: 196px;
    margin: 0;
    font-weight: 300;
    font-size: 46px;
    line-height: 54px;
    letter-spacing: -0.5px;
  }
  .register-badge {
    position: absolute;
    left: 67px;
    top: 409px;
    width: 158px;
    height: 158px;
    box-sizing: border-box;
    border-radius: 50%;
    border: 1px solid #e6e6e6;
    background: var(--brand-blue);
    box-shadow: 0 6px 16px rgba(0, 0, 0, 0.35);
    display: flex;
    align-items: center;
    justify-content: center;
  }
  .register-badge span {
    display: block;
    color: var(--white);
    font-weight: 700;
    font-size: 26px;
    line-height: 31px;
    text-align: center;
    text-transform: uppercase;
    transform: translateY(6px) rotate(4deg);
  }
</style>
</head>
<body>
  <div class="stage">
    <section class="banner" aria-label="Conference banner 300 by 600">
      <div class="shop-illustration" role="img" aria-label="Faint illustration of a mobile shopping app with product tiles and a buy button"></div>
      <h1 class="headline">Have an<br>online<br>business?</h1>
      <p class="subline">Make your<br>customers<br>stick!</p>
      <div class="register-badge"><span>Register<br>now!</span></div>
    </section>
  </div>
</body>
</html>
```